Corvana Wound Care Business card design

We need a business card designed around our logo which was provided. The logo of preference is the colored. Also the colors and fonts were provided.

Target Market(s)

Our Referral partners are home health agencies.

Industry/Entity Type

Healthcare

Contact Information for Business Card

Name , Phone #, Email , Title

Requirements
Nice to have
• Creativity
Should not have
• basic

```html
<!DOCTYPE html>
<html lang="en">
<head>
<meta charset="utf-8">
<title>Corvana Wound Care – Business Card</title>
<link href="https://fonts.googleapis.com/css2?family=Lato:wght@400;700;900&display=swap" rel="stylesheet">
<style>
  :root {
    --navy: #034a8a;
    --navy-deep: #0a3f7f;
    --band: #2d4fa6;
    --sky: #06a3e0;
    --indigo: #2b3a8c;
    --white: #ffffff;
    --page: #ffffff;
  }
  * { margin: 0; padding: 0; box-sizing: border-box; }
  html, body { width: 1200px; height: 1000px; overflow: hidden; background: var(--page); }
  body { position: relative; font-family: "Lato", Arial, sans-serif; }

  .card { position: absolute; left: 254px; width: 693px; overflow: hidden;
          box-shadow: 0 4px 14px rgba(0,0,0,0.22); }

  /* Front */
  .card-front { top: 78px; height: 395px; border-radius: 48px; background: var(--white); }
  .front-bg { position: absolute; inset: 0; }
  .brand-name { position: absolute; left: 0; right: 0; top: 72px; text-align: center;
                color: var(--navy-deep); font-weight: 900; }
  .brand-name .word { display: block; font-size: 64px; line-height: 64px; letter-spacing: 1px; }
  .brand-name .sub { display: block; font-size: 14px; letter-spacing: 8px; margin-top: 8px; }
  .brand-dot { display: inline-block; width: 22px; height: 22px; border-radius: 50%;
               background: var(--navy-deep); margin-right: 12px; vertical-align: 8px; }

  .person { position: absolute; right: 358px; top: 295px; text-align: right; color: var(--white); }
  .person-name { font-size: 25px; font-weight: 900; letter-spacing: 0.5px; line-height: 30px; }
  .person-title { font-size: 16px; font-weight: 400; margin-top: 2px; }
  .divider { position: absolute; left: 360px; top: 290px; width: 1.5px; height: 63px; background: var(--white); }
  .contacts { position: absolute; left: 384px; top: 289px; list-style: none; color: var(--white); font-size: 15.5px; }
  .contacts li { display: flex; align-items: center; height: 21.5px; }
  .contacts svg { width: 12px; height: 12px; margin-right: 10px; flex: none; }

  /* Back */
  .card-back { top: 525px; height: 396px; border-radius: 20px;
               background: linear-gradient(180deg, var(--sky) 0%, #1a6bc4 55%, var(--indigo) 100%); }
  .back-pattern { position: absolute; inset: 0;
                  background: linear-gradient(100deg, rgba(40,240,255,0.25) 0%, rgba(10,30,120,0.15) 60%, rgba(5,10,60,0.35) 100%); }
  .back-brand { position: absolute; left: 444px; top: 270px; color: var(--white); font-weight: 900; }
  .back-brand .word { display: block; font-size: 32px; line-height: 32px; }
  .back-brand .sub { display: block; font-size: 8px; letter-spacing: 4px; margin-top: 4px; }
</style>
</head>
<body>

<section class="card card-front">
  <svg class="front-bg" viewBox="0 0 693 395" preserveAspectRatio="none" aria-hidden="true">
    <path d="M0 170 Q400 303 693 212 L693 395 L0 395 Z" fill="var(--band)"/>
    <path d="M0 186 Q400 306 693 212 L693 395 L0 395 Z" fill="var(--navy)"/>
  </svg>

  <div class="brand-name">
    <span class="word"><span class="brand-dot"></span>corvana</span>
    <span class="sub">WOUND CARE</span>
  </div>

  <div class="person">
    <div class="person-name">DANIEL HART</div>
    <div class="person-title">Founder &amp; CEO</div>
  </div>
  <div class="divider"></div>
  <ul class="contacts">
    <li><svg viewBox="0 0 24 24" aria-hidden="true"><path fill="#fff" d="M6.6 10.8a15 15 0 0 0 6.6 6.6l2.2-2.2c.3-.3.7-.4 1-.2 1.1.4 2.3.6 3.6.6.6 0 1 .4 1 1V20c0 .6-.4 1-1 1A17 17 0 0 1 3 4c0-.6.4-1 1-1h3.5c.6 0 1 .4 1 1 0 1.3.2 2.5.6 3.6.1.3 0 .7-.2 1z"/></svg>(555) 014-2290</li>
    <li><svg viewBox="0 0 24 24" aria-hidden="true"><path fill="#fff" d="M2 5h20v2l-10 7L2 7z M2 9l10 7 10-7v10H2z"/></svg>hello@corvanawound.com</li>
    <li><svg viewBox="0 0 24 24" aria-hidden="true"><circle cx="12" cy="12" r="9" fill="none" stroke="#fff" stroke-width="2.5"/><path fill="none" stroke="#fff" stroke-width="2" d="M3 12h18M12 3c3 3 3 15 0 18M12 3c-3 3-3 15 0 18"/></svg>corvanawound.com</li>
  </ul>
</section>

<section class="card card-back">
  <div class="back-pattern" role="img" aria-label="Repeating brand pattern fading from bright cyan at top left to deep navy at bottom right"></div>
  <div class="back-brand">
    <span class="word">corvana</span>
    <span class="sub">WOUND CARE</span>
  </div>
</section>

</body>
</html>
```